Borvella Gelato Pints

6 flavors , pints italian , southern , organic , natural feel

Pistachio , chocolate, strawberry , hazelnut , vaniglia

Stracciiatelle

Target Market(s)

Upscale

Requirements
Must have
• See graphic upload . Want that look.. showing freshbest quality in gradients of each flavor

```html
<!DOCTYPE html>
<html lang="en">
<head>
<meta charset="utf-8">
<title>Borvella Gelato — Pint Labels</title>
<link rel="stylesheet" href="https://fonts.googleapis.com/css2?family=Dosis:wght@400;500&display=swap">
<style>
  :root {
    --canvas: #ffffff;
    --cream: #f7f3ea;
    --brown: #5a2e1c;
    --brown-dark: #4a2413;
    --white: #ffffff;
    --pistachio-wash: #d9e6c3;
    --chocolate-wash: #e0d9ce;
    --strawberry-wash: #f3cdd0;
  }
  * { margin: 0; padding: 0; box-sizing: border-box; }
  html, body { width: 1200px; height: 776px; overflow: hidden; background: var(--canvas); }
  body { position: relative; font-family: "Dosis", sans-serif; color: var(--brown); }

  .lid {
    position: absolute; top: 51px; width: 278px; height: 278px;
    border-radius: 50%; background: var(--cream);
  }
  .lid__ring {
    position: absolute; inset: 13px; border: 1px solid var(--brown); border-radius: 50%;
  }
  .lid__name {
    position: absolute; left: 0; right: 0; top: 100px; text-align: center;
    font-size: 46px; font-weight: 400; letter-spacing: 1px; line-height: 1;
  }
  .lid__tagline {
    position: absolute; left: 0; right: 0; top: 172px; text-align: center;
    font-size: 17px; font-weight: 500; line-height: 1;
  }

  .label {
    position: absolute; top: 361px; width: 268px; height: 299px; background: var(--cream);
  }
  .label__name {
    position: absolute; left: 0; right: 0; top: 22px; text-align: center;
    font-size: 34px; font-weight: 400; letter-spacing: 1px; line-height: 1;
  }
  .label__tagline {
    position: absolute; left: 0; right: 0; top: 80px; text-align: center;
    font-size: 13px; font-weight: 500; line-height: 1;
  }
  .label__art {
    position: absolute; left: 59px; top: 100px; width: 150px; height: 115px; border-radius: 40%;
  }
  .label__flavor {
    position: absolute; left: 66px; top: 233px; width: 136px; height: 20px;
    border-radius: 3px; text-align: center; font-size: 12px; font-weight: 500;
    letter-spacing: 1.5px; line-height: 20px; text-transform: uppercase;
  }
  .label__volume {
    position: absolute; left: 112px; top: 274px; width: 43px; height: 25px;
    background: var(--brown-dark); color: var(--white);
    font-size: 9px; font-weight: 500; line-height: 25px; text-align: center; letter-spacing: 0.5px;
  }

  .art--pistachio { background: radial-gradient(ellipse at center, #b9cf7a 0%, #e6c9a0 45%, rgba(247,243,234,0) 72%); }
  .art--chocolate { background: radial-gradient(ellipse at center, #4a2418 0%, #6b3a2a 40%, rgba(247,243,234,0) 72%); }
  .art--strawberry { background: radial-gradient(ellipse at center, #d8302c 0%, #e4483f 40%, rgba(247,243,234,0) 72%); }

  .wash--pistachio { background: var(--pistachio-wash); }
  .wash--chocolate { background: var(--chocolate-wash); }
  .wash--strawberry { background: var(--strawberry-wash); }
</style>
</head>
<body>
  <div class="lid" style="left:83px">
    <div class="lid__ring"></div>
    <div class="lid__name">Borvella</div>
    <div class="lid__tagline">ITALIAN GELATO</div>
  </div>
  <div class="lid" style="left:451px">
    <div class="lid__ring"></div>
    <div class="lid__name">Borvella</div>
    <div class="lid__tagline">ITALIAN GELATO</div>
  </div>
  <div class="lid" style="left:819px">
    <div class="lid__ring"></div>
    <div class="lid__name">Borvella</div>
    <div class="lid__tagline">ITALIAN GELATO</div>
  </div>

  <div class="label" style="left:87px">
    <div class="label__name">Borvella</div>
    <div class="label__tagline">ITALIAN GELATO</div>
    <div class="label__art art--pistachio" role="img" aria-label="Watercolour illustration of pistachio nuts"></div>
    <div class="label__flavor wash--pistachio">Pistachio</div>
    <div class="label__volume">473ML</div>
  </div>
  <div class="label" style="left:455px">
    <div class="label__name">Borvella</div>
    <div class="label__tagline">ITALIAN GELATO</div>
    <div class="label__art art--chocolate" role="img" aria-label="Illustration of chocolate pieces and cocoa beans"></div>
    <div class="label__flavor wash--chocolate">Chocolate</div>
    <div class="label__volume">473ML</div>
  </div>
  <div class="label" style="left:822px">
    <div class="label__name">Borvella</div>
    <div class="label__tagline">ITALIAN GELATO</div>
    <div class="label__art art--strawberry" role="img" aria-label="Watercolour illustration of two strawberries"></div>
    <div class="label__flavor wash--strawberry">Strawberry</div>
    <div class="label__volume">473ML</div>
  </div>
</body>
</html>
```